Rex Tollbridge (Burn The Stack) CD Cover Design

Professional Cd cover design needed. No photo of the artist necessary for this cover. You can search Rex Tollbridge on YouTube for a feel of the artist, inspiration, etc. Song (Burn The Stack)!

Target Market(s)

Big money makers , Hustlers, those who don't mind spending cash.

Colors

Designer to choose colors to be used in the design.

Requirements
Nice to have
• Any symbols related to money.

```html
<!DOCTYPE html>
<html lang="en">
<head>
<meta charset="utf-8">
<title>Rex Tollbridge — Burn The Stack</title>
<link rel="stylesheet" href="https://fonts.googleapis.com/css2?family=League+Spartan:wght@700;800&display=swap">
<style>
  :root {
    --bg: #2b2b2b;
    --rule: #ffffff;
    --note-light: #f1f1ee;
    --note-mid: #d6d8d2;
    --note-shade: #bfc3bb;
    --note-green: #b9d9b4;
  }
  html, body {
    margin: 0;
    padding: 0;
    width: 1200px;
    height: 1200px;
    overflow: hidden;
    background: var(--bg);
  }
  .cover {
    display: block;
    width: 1200px;
    height: 1200px;
    background: var(--bg);
  }
  .cover-text {
    font-family: "League Spartan", "Futura", sans-serif;
    font-weight: 800;
    fill: url(#banknote-fill);
  }
  .artist-name { font-weight: 700; }
  .title-center { text-anchor: middle; }
  .divider { fill: var(--rule); }
</style>
</head>
<body>
<svg class="cover" viewBox="0 0 1200 1200" xmlns="http://www.w3.org/2000/svg"
     role="img" aria-label="Lettering filled with a close-up of banknote engraving in pale grey and green tones">
  <defs>
    <linearGradient id="banknote-fill" x1="0" y1="0" x2="1" y2="1">
      <stop offset="0" stop-color="var(--note-light)"/>
      <stop offset="0.3" stop-color="var(--note-mid)"/>
      <stop offset="0.5" stop-color="var(--note-light)"/>
      <stop offset="0.7" stop-color="var(--note-shade)"/>
      <stop offset="0.85" stop-color="var(--note-green)"/>
      <stop offset="1" stop-color="var(--note-light)"/>
    </linearGradient>
  </defs>

  <text class="cover-text artist-name" x="76" y="172" font-size="140"
        textLength="1052" lengthAdjust="spacingAndGlyphs">REX TOLLBRIDGE</text>

  <rect class="divider" x="72" y="209" width="1056" height="11"/>

  <text class="cover-text title-line" x="76" y="500" font-size="340"
        textLength="1052" lengthAdjust="spacingAndGlyphs">BURN</text>

  <text class="cover-text title-line title-center" x="600" y="844" font-size="400">THE</text>

  <text class="cover-text title-line" x="76" y="1120" font-size="310"
        textLength="1052" lengthAdjust="spacingAndGlyphs">STACK</text>
</svg>
</body>
</html>
```